Vortelan d.o.o. needes a web site design

We are a company dealing with automatic doors, industrial doors, roller shutters, access control systems.
We would like to get a design which is clean and neat, and here are some sites which work with similar products. These designs are some we like, but of course, I am looking for a design which is unique. We usually use grey and red colours, which you can see on www.vortelan.ba .
The sites we like are:
http://www.plexawin.com/gb/
http://www.brunosteca.it/eng/
http://faswoodportamel.com/

You have to understand, that we have 4 different groups of products, which are main groups. I would like if those 4 groups somehow could be in different colours. (Maybe "zuvex" colours), in order to separate the groups in some way.

Attached you have web site structure.

If any questions, please contact me.
Edvin

Target Market(s)

Bosnian market. Aluminium and PVC doors and window market, Construction companies, Supermarkets-Retail, Gas stations, Banks, Food industry, Heavy industry.

Industry/Entity Type

It Company

Contact Information for Business Card

I have attached our current business card in PDF. I weould like english on one side, bosnian on other side.

Logo Text

Vortelan is the name of the company, our core business is automation!

Number of Pages Required

5+ page

Font styles to use
Sans Serif

Colors
ec1f27
0792cd
9bcb3c
ffc214
ffffff

```html
<!DOCTYPE html>
<html lang="bs">
<head>
<meta charset="utf-8">
<title>Vortelan d.o.o.</title>
<link href="https://fonts.googleapis.com/css2?family=Roboto:wght@300;400;500;700&display=swap" rel="stylesheet">
<style>
:root{
  --red:#ec1f27;
  --blue:#0792cd;
  --green:#9bcb3c;
  --yellow:#ffc214;
  --white:#ffffff;
  --page:#f2f2f2;
  --dark:#3a3a3a;
  --footer:#232323;
  --field:#333333;
  --text:#555555;
}
*{box-sizing:border-box;margin:0;padding:0}
html,body{width:767px;height:1200px;overflow:hidden}
body{position:relative;background:var(--page);font-family:'Roboto',sans-serif;color:var(--text)}
.abs{position:absolute}
.topline{left:0;top:0;width:767px;height:2px;background:var(--red)}
.brand{left:63px;top:44px;display:flex;align-items:center;gap:8px;font-size:20px;font-weight:700;color:var(--red)}
.brand .mark{width:14px;height:14px;background:var(--dark)}
.lang{left:370px;top:19px;width:117px;height:22px;border:1px solid #ddd;background:#fff;font-size:7px;color:#666;padding:6px 0 0 18px}
.lang .caret{position:absolute;right:0;top:0;width:22px;height:20px;background:var(--dark)}
.lang .caret:after{content:"";position:absolute;left:8px;top:8px;border:3px solid transparent;border-top-color:#fff}
.search{left:494px;top:19px;width:178px;height:22px;border:1px solid #ddd;background:#fff;font-size:7px;color:#777;padding:6px 0 0 8px}
.search-btn{left:674px;top:19px;width:29px;height:22px;background:var(--red)}
.follow{top:64px;display:flex;align-items:center;gap:4px;font-size:7px;color:#444}
.follow .c{width:20px;height:20px;border:1.5px solid #444;border-radius:50%}
.nav{left:63px;top:89px;width:641px;height:36px;background:var(--dark);display:flex;font-size:7.5px;font-weight:500;color:#fff;text-transform:uppercase}
.nav span{display:flex;align-items:center;justify-content:center;padding:0 17px;flex:1 1 auto}
.nav .on{background:var(--red);flex:0 0 65px}
.hero{left:63px;top:133px;width:641px;height:308px;background:linear-gradient(100deg,#2f4a6a 0%,#8aa2bd 35%,#c9d4df 60%,#6f8aa6 100%)}
.arrows{left:667px;top:343px;color:#fff;font-size:20px;font-weight:300;letter-spacing:2px}
.caption{left:63px;top:374px;width:531px;height:67px;background:rgba(236,31,39,.82);color:#fff;padding:12px 21px}
.caption h2{font-size:13px;font-weight:400;margin-bottom:6px}
.caption p{font-size:7px;line-height:12.5px;font-weight:300}
.cta{left:594px;top:374px;width:110px;height:67px;background:rgba(50,50,50,.9);color:#fff;font-size:9.5px;font-weight:500;display:flex;align-items:center;justify-content:center}
.sec-title{left:0;width:767px;text-align:center;font-size:15px;color:#333}
.sec-title span{display:inline-block;padding:0 30px 4px;border-bottom:1px solid var(--red)}
.lead{left:140px;top:503px;width:487px;text-align:center;font-size:7.5px;line-height:15.5px;color:#555}
.card{top:551px;width:145px;height:198px;background:#fff;text-align:center;border-bottom:2px solid}
.card .img{height:98px;margin:1px}
.card h3{font-size:8px;font-weight:400;margin:13px 0 6px}
.card p{font-size:6.5px;line-height:13px;color:#777;padding:0 8px}
.card a{display:inline-block;margin-top:8px;font-size:7px;font-weight:500;text-decoration:underline}
.news{left:63px;top:778px;width:641px;height:189px;background:#fff;border:1px solid #e6e6e6}
.news p{position:absolute;left:12px;top:58px;width:615px;text-align:center;font-size:7.5px;line-height:16.5px}
.news .date{position:absolute;left:0;top:112px;width:639px;text-align:center;font-size:8.5px;font-weight:500;color:var(--red)}
.news .btn{position:absolute;left:256px;top:137px;width:129px;height:30px;background:var(--red);border-radius:3px;color:#fff;font-size:8.5px;font-weight:500;display:flex;align-items:center;justify-content:center}
.footer{left:0;top:998px;width:767px;height:202px;background:var(--footer);border-top:2px solid var(--red)}
.ft{top:1022px;font-size:10px;color:#fff}
.field{left:63px;width:172px;height:21px;background:var(--field);color:#ddd;font-size:7px;padding:6px 7px}
.msg{left:242px;top:1051px;width:172px;height:42px;background:var(--field);color:#ddd;font-size:7px;padding:5px 7px}
.agree{left:242px;top:1107px;width:100px;font-size:5.5px;line-height:9px;color:#888;padding-left:10px}
.agree:before{content:"";position:absolute;left:0;top:1px;width:5px;height:5px;border:1px solid #888}
.send{left:345px;top:1105px;width:69px;height:22px;background:var(--red);border-radius:2px;color:#fff;font-size:7.5px;font-weight:500;display:flex;align-items:center;justify-content:center}
.contact{left:457px;top:1051px;width:247px;height:79px;background:var(--field);font-size:6.5px;color:#ddd}
.contact div{position:absolute;display:flex;align-items:center;gap:4px}
.contact i{display:inline-block;width:6px;height:6px;background:#ddd;border-radius:50%}
.rule{left:63px;top:1156px;width:641px;height:1px;background:#333}
.copy{left:63px;top:1172px;font-size:6.5px;color:#aaa}
.footer-follow{color:#888}
.footer-follow .c{border-color:#666}
</style>
</head>
<body>
<div class="abs topline"></div>

<header>
  <div class="abs brand"><span class="mark"></span>Vortelan d.o.o.</div>
  <div class="abs lang">Choose a Language<span class="caret"></span></div>
  <div class="abs search">traži</div>
  <div class="abs search-btn">
    <svg width="29" height="22" viewBox="0 0 29 22"><circle cx="14" cy="10" r="3" fill="none" stroke="#fff" stroke-width="1.4"/><line x1="16" y1="12" x2="18" y2="14" stroke="#fff" stroke-width="1.4"/></svg>
  </div>
  <div class="abs follow" style="left:555px">Prati nas:<span class="c"></span><span class="c"></span><span class="c"></span><span class="c"></span><span class="c"></span></div>
  <nav class="abs nav">
    <span class="on">Home</span><span>Automatska vrata</span><span>Industrijska vrata</span><span>Rolo vrata</span><span>Kontrola pristupa</span><span>Referentna</span><span>Kontakt</span>
  </nav>
</header>

<section>
  <div class="abs hero" role="img" aria-label="Photo of glass automatic sliding doors in a modern building lobby"></div>
  <div class="abs arrows">‹ ›</div>
  <div class="abs caption">
    <h2>AUTOMATSKA KLIZNA VRATA</h2>
    <p>Sed ut perspiciatis unde omnis iste natus error sit voluptatem accusantium doloremque laudantium, totam rem aperiam, eaque ipsa quae ab illo inventore veritatis et quasi architecto beatae vitae dicta sunt explicabo...</p>
  </div>
  <div class="abs cta">KLIKNITE OVDJE</div>
</section>

<section>
  <div class="abs sec-title" style="top:472px"><span>Istaknuti Proizvodi</span></div>
  <p class="abs lead">Sed ut perspiciatis unde omnis iste natus error sit voluptatem accusantium doloremque laudantium, totam rem aperiam, eaque ipsa quae ab illo inventore veritatis et quasi architecto beatae...</p>

  <article class="abs card" style="left:63px;border-color:var(--red)">
    <div class="img" role="img" aria-label="Red-tinted photo of an automatic entrance door" style="background:linear-gradient(160deg,#e87a80,#c9474f)"></div>
    <h3 style="color:var(--red)">AUTOMATSKA VRATA</h3>
    <p>It is a long established fact that a reader will be distracted by the read it look like readable English...</p>
    <a style="color:var(--red)">ČITAJ VIŠE</a>
  </article>
  <article class="abs card" style="left:228px;border-color:var(--blue)">
    <div class="img" role="img" aria-label="Blue-tinted photo of an industrial sectional door" style="background:linear-gradient(160deg,#4a8fd0,#2a62a8)"></div>
    <h3 style="color:var(--blue)">INDUSTRIJSKA VRATA</h3>
    <p>It is a long established fact that a reader will be distracted by the read it look like readable English...</p>
    <a style="color:var(--blue)">ČITAJ VIŠE</a>
  </article>
  <article class="abs card" style="left:393px;border-color:var(--green)">
    <div class="img" role="img" aria-label="Green-tinted photo of a roller shutter door in a warehouse" style="background:linear-gradient(160deg,#b6d66a,#7ea52e)"></div>
    <h3 style="color:var(--green)">ROLO VRATA</h3>
    <p>It is a long established fact that a reader will be distracted by the read it look like readable English...</p>
    <a style="color:var(--green)">ČITAJ VIŠE</a>
  </article>
  <article class="abs card" style="left:557px;border-color:var(--yellow)">
    <div class="img" role="img" aria-label="Yellow-tinted photo of an access control keypad terminal" style="background:linear-gradient(160deg,#f3d271,#d9a92c)"></div>
    <h3 style="color:var(--yellow)">KONTROLA PRISTUPA</h3>
    <p>It is a long established fact that a reader will be distracted by the read it look like readable English...</p>
    <a style="color:var(--yellow)">ČITAJ VIŠE</a>
  </article>
</section>

<section class="abs news">
  <div class="abs sec-title" style="top:21px;width:639px"><span>News Feed</span></div>
  <p>Sed ut perspiciatis unde omnis iste natus error sit voluptatem accusantium doloremque laudantium, totam rem aperiam, eaque ipsa quae ab illo inventore veritatis et quasi architecto beatae vitae dicta sunt explicabo. Nemo enim ipsam voluptatem quia voluptas sit aspernatur aut odit aut fugit, sed quia consequuntur magni dolores eos qui ratione voluptatem sequi nesciunt. Neque porro quisquam est, qui dolorem ipsum quia dolor sit amet, consectetur, adipisci velit, sed quia non numquam eius modi tempora incidunt</p>
  <div class="date">Pošta na ožujak 04 2016</div>
  <div class="btn">Pročitajte više informacija</div>
</section>

<footer>
  <div class="abs footer"></div>
  <div class="abs ft" style="left:63px">Bilten</div>
  <div class="abs ft" style="left:457px">Kontakt</div>
  <div class="abs field" style="top:1051px">ime</div>
  <div class="abs field" style="top:1079px">E-mail</div>
  <div class="abs field" style="top:1106px">adresa</div>
  <div class="abs msg">poruka...</div>
  <div class="abs agree">Izjavljujem da sam pročitao i složili se privatnost Odricanje</div>
  <div class="abs send">Podnijeti</div>
  <div class="abs contact">
    <div style="left:12px;top:12px"><i></i>Lipova bb, 74000 Sutjeska, Bosna i Hercegovina</div>
    <div style="left:12px;top:37px"><i></i>T:+387 55 410 220 &nbsp;<i></i>F:+387 55 410 221 &nbsp;<i></i>M:+387 65 318 470</div>
    <div style="left:12px;top:61px"><i></i>@: info@vortelan.ba &nbsp;&nbsp;<i></i>w: www.vortelan.ba</div>
  </div>
  <div class="abs rule"></div>
  <div class="abs copy">©vortelan.2016 | Sva prava pridržana</div>
  <div class="abs follow footer-follow" style="left:555px;top:1166px">Prati nas:<span class="c"></span><span class="c"></span><span class="c"></span><span class="c"></span><span class="c"></span></div>
</footer>
</body>
</html>
```